KL Taxidermy

I need business Cards with my logo and a background photo of one of my taxidermy mounts.
I would like a black back drop behind it all and what ever looks best for my contact information (red or white?)
Garrick Pembley
592-718-4409
kltaxidermy482@mailnook.example
Chatterloom page

```html
<!DOCTYPE html>
<html lang="en">
<head>
<meta charset="utf-8">
<title>KL Taxidermy – Business Card</title>
<link href="https://fonts.googleapis.com/css2?family=Archivo+Black&family=Arimo:wght@400;700&display=swap" rel="stylesheet">
<style>
  :root {
    --ink: #161415;
    --card-black: #231f20;
    --paper: #ffffff;
    --accent-red: #c4161c;
    --muted: #4a4a4a;
    --stage: #ececec;
    --faint-mark: #2f2b2c;
  }
  * { box-sizing: border-box; margin: 0; padding: 0; }
  html, body { width: 1200px; height: 1200px; overflow: hidden; }
  body {
    background: var(--stage);
    font-family: "Arimo", Arial, sans-serif;
    display: flex; flex-direction: column; align-items: center; justify-content: center;
    gap: 40px;
  }
  .card {
    width: 960px; height: 549px; position: relative; overflow: hidden;
    box-shadow: 0 6px 24px rgba(0,0,0,.18);
  }

  /* Front: black backdrop with mount photo */
  .card--front { background: var(--card-black); }
  .front__mark {
    position: absolute; top: 70px; left: 560px;
    display: flex; align-items: center; gap: 12px;
    color: var(--faint-mark); font-weight: 700; font-size: 28px; letter-spacing: 3px;
    text-transform: uppercase;
  }
  .front__mark-dot { width: 34px; height: 34px; border-radius: 50%; background: var(--faint-mark); }
  .front__photo {
    position: absolute; left: 70px; top: 160px; width: 760px; height: 330px;
    border-radius: 160px 200px 40px 120px;
    background: radial-gradient(ellipse at 55% 40%, #e6e4df 0%, #c9c7c2 40%, #6b6d71 75%, rgba(35,31,32,0) 100%);
  }

  /* Back: white contact side */
  .card--back { background: var(--paper); color: var(--ink); }
  .back__logo {
    position: absolute; top: 70px; left: 0; right: 0;
    display: flex; justify-content: center; align-items: center; gap: 14px;
    font-weight: 700; font-size: 34px; letter-spacing: 4px; text-transform: uppercase;
  }
  .back__logo-mark { width: 44px; height: 44px; border-radius: 50%; background: var(--ink); }
  .back__identity { position: absolute; top: 170px; left: 0; right: 0; text-align: center; }
  .back__name { font-family: "Archivo Black", sans-serif; font-size: 38px; }
  .back__role { color: var(--accent-red); font-size: 30px; margin-top: 2px; }

  .pill {
    position: absolute; width: 110px; height: 62px; background: var(--ink);
    display: flex; align-items: center; justify-content: center;
  }
  .pill--email { right: 0; top: 300px; border-radius: 31px 0 0 31px; padding-left: 8px; justify-content: flex-start; }
  .pill--phone { left: 0; top: 430px; border-radius: 0 31px 31px 0; padding-right: 8px; justify-content: flex-end; }
  .pill svg { width: 30px; height: 30px; margin: 0 22px; }

  .back__email { position: absolute; right: 130px; top: 312px; font-size: 30px; }
  .back__phone { position: absolute; left: 130px; top: 438px; font-size: 36px; font-weight: 700; }
  .back__cta {
    position: absolute; left: 400px; top: 446px;
    font-family: "Archivo Black", sans-serif; font-size: 24px; color: var(--muted); letter-spacing: 1px;
  }
  .back__social {
    position: absolute; left: 620px; top: 400px;
    display: flex; align-items: center; gap: 10px; font-size: 22px; text-transform: uppercase;
  }
  .back__social-dot { width: 22px; height: 22px; border: 2px solid var(--ink); border-radius: 50%; }
</style>
</head>
<body>
  <section class="card card--front">
    <div class="front__mark"><span class="front__mark-dot"></span>KL Taxidermy</div>
    <div class="front__photo" role="img" aria-label="Photo of a white Dall sheep ram taxidermy mount lying on a grey rock base"></div>
  </section>

  <section class="card card--back">
    <div class="back__logo"><span class="back__logo-mark"></span>KL Taxidermy</div>
    <div class="back__identity">
      <div class="back__name">Garrick Pembley</div>
      <div class="back__role">Position Here</div>
    </div>

    <div class="pill pill--email">
      <svg viewBox="0 0 30 30" fill="none" stroke="#fff" stroke-width="2"><rect x="4" y="8" width="22" height="15" rx="1"/><path d="M4 9l11 8 11-8"/></svg>
    </div>
    <div class="back__email">kltaxidermy482@mailnook.example</div>

    <div class="back__social"><span class="back__social-dot"></span>Chatterloom</div>

    <div class="pill pill--phone">
      <svg viewBox="0 0 30 30" fill="none" stroke="#fff" stroke-width="2"><rect x="9" y="3" width="12" height="24" rx="2"/><path d="M13 23h4"/></svg>
    </div>
    <div class="back__phone">592-718-4409</div>
    <div class="back__cta">GET IN TOUCH</div>
  </section>
</body>
</html>
```